Web Design Project - Old Brackley (Bar)

We need a website for a new wine bar/hotel opening in Sydney's Kings Cross area. The concept is a rustic Australiana bar. We intend to use raw materials (sandstone, rusty metal etc) and lots of greenery/plants. It is set to be stylish and accessible to a young and middle age clientele.

The idea is to bring the outside inside.

The venue can cater for 450 people and is in one of the major nightclub strips in Australia. The demographic differs from celebrities to backpackers.

Target Market(s)

We are targeting 23yr - 40yr olds.

Industry/Entity Type

Hotel

Requirements
Must have
• What I want is a design to reflect is the fit out of the bar. We would like to see a rustic design to reflect the theme of the bar. The theme behind the fit out will be "bringing the outside inside" with lots of plants, wet walls etc.. There will be exposed brickwork, sandstone, timber and rusted steel with laser cut designs throughout the venue.
Nice to have
• I've attached some 3D designs that the venue will be roughly based on.

```html
<!DOCTYPE html>
<html lang="en">
<head>
<meta charset="utf-8">
<title>Old Brackley – Contact</title>
<link rel="stylesheet" href="https://fonts.googleapis.com/css2?family=Noticia+Text:wght@400;700&family=Open+Sans:wght@400;600;700&display=swap">
<style>
  :root {
    --wood-dark: #2e1c10;
    --wood-mid: #5a4430;
    --header-wood: #9c8264;
    --header-wood-light: #b59e80;
    --bark: #3a1300;
    --sand: #dcbf8e;
    --parchment: #f2ddb5;
    --button: #dcbf8e;
    --crimson: #a8090c;
    --maroon: #6e0b0e;
    --nav-text: #e6c18c;
    --nav-active: #fbeed6;
    --ink: #222;
    --leather: #b08a52;
    --leather-dark: #7a5a30;
    --cream: #ffffff;
  }
  * { box-sizing: border-box; margin: 0; padding: 0; }
  html, body { width: 1003px; height: 1200px; overflow: hidden; }
  body { font-family: "Open Sans", Arial, sans-serif; background: var(--wood-dark); }
  .page { position: relative; width: 1003px; height: 1200px; overflow: hidden; }

  .wood-top {
    position: absolute; left: 0; top: 0; width: 1003px; height: 77px;
    background: linear-gradient(90deg, #4a3826, #6a543c 30%, #3e2e1e 55%, #5e4a34 80%, #3a2a1a);
  }
  .header-rule { position: absolute; left: 0; top: 77px; width: 1003px; height: 10px; background: var(--bark); }
  .masthead {
    position: absolute; left: 0; top: 87px; width: 1003px; height: 205px;
    background: radial-gradient(ellipse at 50% 40%, var(--header-wood-light), var(--header-wood) 55%, #6a5038);
  }
  .brand {
    position: absolute; left: 0; right: 0; top: 118px; text-align: center;
    font-family: "Noticia Text", Georgia, serif; font-weight: 400;
    font-size: 40px; letter-spacing: 3px; color: #1a120c;
  }

  .nav {
    position: absolute; left: 0; top: 295px; width: 1003px; height: 55px;
    background: var(--bark);
    border-top: 1px dashed rgba(230,193,140,0.6);
    border-bottom: 1px dashed rgba(230,193,140,0.6);
    display: flex; justify-content: space-between; align-items: center;
    padding: 0 52px 0 82px;
  }
  .nav a {
    color: var(--nav-text); text-decoration: none; font-weight: 700;
    font-size: 17px; letter-spacing: 0.3px;
  }
  .nav a.is-current { color: var(--nav-active); }

  .content { position: absolute; left: 0; top: 350px; width: 1003px; height: 512px; background: var(--sand); }
  .page-title {
    position: absolute; left: 37px; top: 28px;
    font-family: "Noticia Text", Georgia, serif; font-weight: 700;
    font-size: 56px; color: var(--maroon); line-height: 1;
  }
  .contact-card {
    position: absolute; left: 38px; top: 108px; width: 928px; height: 363px;
    background: var(--parchment); border: 1px solid var(--bark); border-radius: 4px;
  }
  .venue-name {
    position: absolute; left: 30px; top: 30px;
    font-family: "Noticia Text", Georgia, serif; font-size: 28px; color: var(--crimson);
  }
  .venue-details { position: absolute; left: 30px; top: 75px; font-size: 14px; line-height: 20px; color: var(--ink); }
  .venue-details dt { font-weight: 700; }
  .venue-details dd { margin-bottom: 18px; }
  .map {
    position: absolute; left: 318px; top: 32px; width: 579px; height: 297px;
    background: linear-gradient(135deg, #e8e2d6 0%, #ddd7c9 55%, #a9c7f0 75%, #c6dbf5 100%);
  }

  .footer-band {
    position: absolute; left: 0; top: 862px; width: 1003px; height: 250px;
    background: var(--bark);
    border-top: 1px dashed rgba(230,193,140,0.6);
    border-bottom: 1px dashed rgba(230,193,140,0.6);
  }
  .info-card {
    position: absolute; top: 41px; height: 164px; width: 290px;
    background: var(--parchment); border-radius: 3px; text-align: center; color: var(--ink);
  }
  .info-card h2 {
    font-family: "Noticia Text", Georgia, serif; font-weight: 400;
    font-size: 30px; color: var(--bark); margin-top: 30px; line-height: 1.1;
  }
  .info-card p { font-size: 14px; line-height: 19px; }
  .info-card--where { left: 37px; }
  .info-card--hours { left: 355px; }
  .info-card--chef { left: 676px; }
  .info-card--chef h2 { margin-top: 30px; }
  .info-card--chef p { padding: 0 18px; }
  .directions {
    display: block; margin: 8px auto 0; width: 246px; height: 40px; line-height: 40px;
    background: var(--button); border-radius: 3px; text-decoration: none;
    font-family: "Noticia Text", Georgia, serif; font-size: 18px; color: var(--crimson);
  }
  .hours-time { font-family: "Noticia Text", Georgia, serif; font-size: 20px; color: var(--crimson); margin-top: 14px; }

  .footer-strip {
    position: absolute; left: 0; top: 1116px; width: 1003px; height: 62px;
    background: linear-gradient(90deg, var(--leather-dark), var(--leather) 40%, #c29a5c 60%, var(--leather-dark));
  }
  .copyright { position: absolute; left: 32px; top: 20px; font-size: 14px; color: var(--cream); }
  .social { position: absolute; right: 28px; top: 20px; display: flex; gap: 10px; }
  .social span { width: 20px; height: 20px; border-radius: 50%; background: var(--cream); display: block; }
  .wood-bottom { position: absolute; left: 0; top: 1178px; width: 1003px; height: 22px; background: #3e2e1e; }
</style>
</head>
<body>
<div class="page">
  <div class="wood-top" role="img" aria-label="Weathered timber planks"></div>
  <div class="header-rule"></div>
  <header class="masthead" role="img" aria-label="Rustic wooden board behind the venue name">
    <div class="brand">OLD BRACKLEY</div>
  </header>

  <nav class="nav">
    <a href="#">HOME</a>
    <a href="#">ABOUT US</a>
    <a href="#">MENU</a>
    <a href="#">RESERVATIONS</a>
    <a href="#" class="is-current">LOCATION</a>
  </nav>

  <main class="content">
    <h1 class="page-title">Contact</h1>
    <section class="contact-card">
      <h2 class="venue-name">OLD BRACKLEY</h2>
      <dl class="venue-details">
        <dt>Address:</dt>
        <dd>418 Ironbark Lane<br>Sydney, AU 2011</dd>
        <dt>Open every day</dt>
        <dd>12:00pm-1:00am</dd>
        <dt>Contacts:</dt>
        <dd>Tel:&nbsp; 1-800-555-0142</dd>
      </dl>
      <div class="map" role="img" aria-label="Street map of inner Sydney with a pin marking Old Brackley"></div>
    </section>
  </main>

  <section class="footer-band">
    <article class="info-card info-card--where">
      <h2>WHERE ARE WE?</h2>
      <p>418 Ironbark Lane, Sydney, AU 2011</p>
      <a href="#" class="directions">GET DIRECTIONS NOW</a>
    </article>
    <article class="info-card info-card--hours">
      <h2>OPENING HOURS</h2>
      <p>We're open everyday</p>
      <p class="hours-time">12:00pm-1:00am</p>
    </article>
    <article class="info-card info-card--chef">
      <h2>CHEF AT HOME</h2>
      <p>I'm a Paragraph. Click here to add your own text and edit me. It's easy. Just click “Edit Text”</p>
    </article>
  </section>

  <footer class="footer-strip" role="img" aria-label="Worn leather texture band">
    <p class="copyright">© 2013 by Old Brackley.</p>
    <div class="social" aria-label="Social links"><span></span><span></span><span></span></div>
  </footer>
  <div class="wood-bottom" role="img" aria-label="Weathered timber planks"></div>
</div>
</body>
</html>
```